Business card: GREEN HERONS TRADE SUPPLY

Hello,

This is your mission:

-I've just done my logo on the website. Now, I need A BUSINESS CARD.
-2 same business cards for 2 persons
-Landscape
-Dimension of the business card: 8.5 cm long and 5 cm high
-Different front and back
-For your information: this new company is selling products (fashion accessories, electronics, watches, fragrances, sunglasses, etc. to large clients related to shops in airlines (inflight catalogue), airports, cruises, etc.
-Colors and logo: please use the same colors of the logo attached (in blue with orange details) and follow the spirit of the existing logo.

-Front:
-1st person:
GREEN HERONS s.p.r.l.
Travel Retail Agency
www.greenheronsx.com
Lucien DEMARBAIX
Partner
Mobile: +32488316257
Email: ld@greenheronsx.com
-2nd person:
GREEN HERONS s.p.r.l.
Travel Retail Agency
www.greenheronsx.com
Joris VANMECHELEN
Partner
Mobile: +32488625170
Email: jv@greenheronsx.com

-Back
Logo
see attached file. Please use the colors of the logo in blue with orange details.

Reason: I increase time necause i don t know if the deadline is in usa time or european time. I will make the selection at 9pm belgian time.

I'm selling products to large accounts/clients. Some of them do more than 2 Billion eur turnover

Airlines

Must have
• Use the logo.
The buyers get so many business cards.
They should remember me easily.
This is why my logo/company name is a stork and a color. 2 things that people usually remember easily.

```html
<!DOCTYPE html>
<html lang="en">
<head>
<meta charset="utf-8">
<title>Green Herons Trade Supply – Business Card</title>
<link rel="stylesheet" href="https://fonts.googleapis.com/css2?family=Exo+2:wght@400;600;700&display=swap">
<style>
  :root {
    --bg: #e9e8e6;
    --paper: #f7f7f5;
    --navy: #2c2f7a;
    --teal: #2a8db3;
    --ink: #2a7fa6;
    --shadow: rgba(0, 0, 0, 0.14);
  }
  * { margin: 0; padding: 0; box-sizing: border-box; }
  html, body {
    width: 1200px;
    height: 873px;
    overflow: hidden;
    background: var(--bg);
    font-family: "Exo 2", Arial, sans-serif;
  }
  .sheet {
    position: relative;
    width: 1200px;
    height: 873px;
  }
  .card {
    position: absolute;
    top: 286px;
    width: 510px;
    height: 300px;
    background: var(--paper);
    box-shadow: 0 6px 18px var(--shadow);
    overflow: hidden;
  }
  .card--front { left: 60px; }
  .card--back { left: 630px; }

  /* front */
  .card__band {
    position: absolute;
    inset: 0;
    width: 100%;
    height: 100%;
  }
  .brand {
    position: absolute;
    left: 34px;
    top: 38px;
    display: flex;
    align-items: center;
    gap: 8px;
  }
  .brand__mark {
    width: 10px;
    height: 10px;
    background: var(--navy);
    flex: none;
  }
  .brand__name {
    font-weight: 600;
    color: var(--navy);
    font-size: 15px;
    line-height: 1;
    white-space: nowrap;
  }
  .person {
    position: absolute;
    left: 34px;
    top: 112px;
  }
  .person__name {
    font-weight: 700;
    font-size: 19px;
    color: var(--ink);
    margin-bottom: 14px;
  }
  .contact {
    list-style: none;
    font-size: 13px;
    color: var(--ink);
    font-weight: 600;
  }
  .contact li {
    display: flex;
    align-items: center;
    gap: 10px;
    height: 26px;
  }
  .contact__icon {
    width: 18px;
    height: 18px;
    flex: none;
    fill: var(--navy);
  }
  .contact__at {
    width: 18px;
    text-align: center;
    font-size: 19px;
    font-weight: 700;
    color: var(--navy);
  }

  /* back */
  .logo-block {
    position: absolute;
    inset: 0;
    display: flex;
    align-items: center;
    justify-content: center;
    gap: 12px;
  }
  .logo-block__mark {
    width: 16px;
    height: 16px;
    background: var(--navy);
    flex: none;
  }
  .logo-block__name {
    font-weight: 600;
    color: var(--navy);
    font-size: 30px;
    line-height: 1;
    white-space: nowrap;
  }
</style>
</head>
<body>
<main class="sheet">

  <section class="card card--front" aria-label="Business card front">
    <svg class="card__band" viewBox="0 0 510 300" preserveAspectRatio="none" aria-hidden="true">
      <path d="M370 0 C 410 110, 400 220, 330 300 L 510 300 L 510 0 Z" fill="var(--teal)"/>
      <path d="M392 0 C 430 110, 420 220, 350 300 L 510 300 L 510 0 Z" fill="var(--navy)"/>
    </svg>

    <div class="brand">
      <span class="brand__mark"></span>
      <span class="brand__name">Green Herons Trade Supply</span>
    </div>

    <div class="person">
      <p class="person__name">Lucien DEMARBAIX</p>
      <ul class="contact">
        <li>
          <svg class="contact__icon" viewBox="0 0 24 24" aria-hidden="true">
            <path d="M6.6 10.8a15.1 15.1 0 0 0 6.6 6.6l2.2-2.2a1 1 0 0 1 1-.25 11.4 11.4 0 0 0 3.6.57 1 1 0 0 1 1 1V20a1 1 0 0 1-1 1A17 17 0 0 1 3 4a1 1 0 0 1 1-1h3.5a1 1 0 0 1 1 1c0 1.25.2 2.45.57 3.57a1 1 0 0 1-.25 1z"/>
          </svg>
          <span>+32488316257</span>
        </li>
        <li>
          <span class="contact__at" aria-hidden="true">@</span>
          <span>ld@greenheronsx.com</span>
        </li>
        <li>
          <svg class="contact__icon" viewBox="0 0 24 24" aria-hidden="true">
            <path d="M4 3 L20 10 L13 12 L10 20 Z"/>
          </svg>
          <span>www.greenheronsx.com</span>
        </li>
      </ul>
    </div>
  </section>

  <section class="card card--back" aria-label="Business card back">
    <div class="logo-block">
      <span class="logo-block__mark"></span>
      <p class="logo-block__name">Green Herons Trade Supply</p>
    </div>
  </section>

</main>
</body>
</html>
```